Home Security Website

This website is for a home security website. We feature the best in home security products and monitoring. The website name is Porchlight Partners.
We would like a direct response design with a large hero image.
The final design should incorporate safety, security, and family. Please do not use scare tactics in the design.
Target Market(s)
Women, primarily
Industry/Entity Type
Security
Requirements
Must have
- Must have a clear Call to Action Area for telephone and lead gen form
Nice to have
- - Large heroes with lifestyle images of family - security
- below the fold text area with boxes
Should not have
- no scare tactics please
DO NOT submit designs with DARK or BLACK backgrounds

```html
<!DOCTYPE html>
<html lang="en">
<head>
<meta charset="utf-8">
<title>Porchlight Partners – Home Security</title>
<link rel="stylesheet" href="https://fonts.googleapis.com/css2?family=Oswald:wght@500;700&family=Roboto+Condensed:wght@400;700&family=Arimo:wght@400;700&display=swap">
<style>
:root{
  --blue:#0098d9;
  --blue-light:#2fb2ea;
  --blue-dark:#0077ae;
  --red:#c40d10;
  --red-dark:#8f0508;
  --gray-band:#646464;
  --gray-text:#555;
  --white:#fff;
  --brown:#6a4630;
  --orange:#f5a50c;
}
*{box-sizing:border-box;margin:0;padding:0}
html,body{width:1200px;height:1194px;overflow:hidden;background:var(--white);font-family:"Arimo",Arial,sans-serif}
.page{position:relative;width:1200px;height:1194px}
.abs{position:absolute}

.topbar{left:0;top:0;width:1200px;height:49px;background:var(--blue);border-bottom:4px solid var(--blue-light)}
.navband{left:0;top:53px;width:1200px;height:37px;background:linear-gradient(#fafafa,#ececec);border-bottom:1px solid #d6d6d6}
.brand-tab{left:131px;top:0;width:93px;height:113px;background:var(--white);box-shadow:0 2px 4px rgba(0,0,0,.25);clip-path:polygon(0 0,100% 0,100% 92%,0 100%)}
.brand-mark{left:158px;top:28px;width:40px;height:40px;background:var(--red)}
.brand-name{left:251px;top:13px;color:var(--white);font-family:"Roboto Condensed",sans-serif;font-weight:700;font-size:24px;letter-spacing:-.3px}

.search{left:793px;top:14px;width:204px;height:24px;background:var(--blue-dark);border-radius:3px;color:#cfe9f7;font-family:"Roboto Condensed",sans-serif;font-size:13px;padding:3px 8px;display:flex;justify-content:space-between;align-items:center}
.login{left:1007px;top:14px;width:63px;height:23px;background:var(--red);border-radius:2px;color:var(--white);font-family:"Roboto Condensed",sans-serif;font-size:14px;text-align:center;line-height:23px}

.nav{left:0;top:53px;height:37px;width:1200px;font-family:"Roboto Condensed",sans-serif;font-size:15px;color:var(--blue)}
.nav span{position:absolute;top:10px;white-space:nowrap}
.nav .current{background:#5a5a5a;color:var(--white);border-radius:3px;padding:1px 7px;top:9px}

.hero{left:0;top:90px;width:1200px;height:597px;background:linear-gradient(100deg,#efeee9 0%,#d9d3c6 25%,#b99a80 45%,#e7dc9a 65%,#c79a6a 85%,#f2efe6 100%)}
.band{left:0;top:687px;width:1200px;height:211px;background:var(--gray-band);border-bottom:4px solid #8b8b8b}

.slogan{font-family:"Oswald",sans-serif;font-weight:700;font-size:50px;line-height:78px;height:78px;color:var(--white);padding:0 18px;white-space:nowrap;letter-spacing:-.5px}
.slogan-1{left:131px;top:433px;background:var(--brown)}
.slogan-2{left:143px;top:531px;background:var(--blue)}
.slogan-3{left:162px;top:628px;background:var(--orange)}

.welcome{left:136px;top:727px;color:var(--white);font-family:"Oswald",sans-serif;font-weight:700;font-size:46px;line-height:62px;letter-spacing:1px}
.intro{left:131px;top:801px;width:619px;height:130px;background:linear-gradient(#fff,#f2f2f2);border:1px solid #cfcfcf;padding:15px 17px;font-size:12.4px;line-height:16.3px;color:var(--gray-text)}
.intro::before{content:"";position:absolute;left:14px;top:-9px;border:9px solid transparent;border-top:0;border-bottom-color:var(--white)}

.callbox{left:772px;top:602px;width:298px;height:329px;background:linear-gradient(#fff,#f1f1f1);border:1px solid #cfcfcf;box-shadow:0 1px 3px rgba(0,0,0,.15)}
.call-title{left:0;top:0;width:298px;height:43px;text-align:center;font-family:"Oswald",sans-serif;font-weight:700;font-size:34px;line-height:46px;color:#666;letter-spacing:1px}
.call-phone{left:0;top:43px;width:298px;height:47px;background:repeating-linear-gradient(135deg,var(--red) 0 3px,#b20a0d 3px 5px);color:var(--white);font-family:"Oswald",sans-serif;font-weight:700;font-size:36px;line-height:47px;display:flex;align-items:center;gap:8px;padding-left:18px}
.field{position:absolute;left:15px;width:265px;height:25px;background:var(--white);border:1px solid #c8c8c8;font-size:12px;color:#aaa;padding:5px 10px}
.submit{left:196px;top:286px;width:84px;height:32px;background:linear-gradient(var(--red),var(--red-dark));border:1px solid #777;color:var(--white);font-family:"Oswald",sans-serif;font-weight:700;font-size:19px;text-align:center;line-height:30px}

.products{left:131px;top:972px;width:938px;height:112px}
.product{position:absolute;top:0;height:112px;text-align:center;font-family:"Roboto Condensed",sans-serif;font-weight:700;font-size:14px;color:var(--blue);letter-spacing:.2px}
.product + .product{border-left:1px solid #d8d8d8}
.product .shot{width:96px;height:74px;margin:14px auto 0;border-radius:6px;background:linear-gradient(#f4f4f4,#d9d9d9)}

.footer{left:0;top:1135px;width:1200px;height:59px;background:var(--blue);color:var(--white);font-size:12px}
.footer .copy{position:absolute;left:131px;top:20px}
.footer .links{position:absolute;right:135px;top:20px}
</style>
</head>
<body>
<div class="page">
  <header>
    <div class="abs topbar"></div>
    <div class="abs navband"></div>
    <div class="abs brand-tab"></div>
    <div class="abs brand-mark"></div>
    <div class="abs brand-name">Porchlight Partners</div>
    <div class="abs search"><span>SEARCH</span>
      <svg width="14" height="14" viewBox="0 0 14 14"><circle cx="5.5" cy="5.5" r="4" fill="none" stroke="#cfe9f7" stroke-width="1.6"/><line x1="8.5" y1="8.5" x2="13" y2="13" stroke="#cfe9f7" stroke-width="2"/></svg>
    </div>
    <div class="abs login">LOGIN</div>
    <nav class="abs nav">
      <span class="current" style="left:250px">HOME</span>
      <span style="left:322px">ALARM SYSTEMS</span>
      <span style="left:452px">HOME AUTOMATION</span>
      <span style="left:601px">ENVIRONMENT CONTROLS</span>
      <span style="left:785px">CHILD SAFETY</span>
      <span style="left:896px">ABOUT US</span>
      <span style="left:987px">CONTACT US</span>
    </nav>
  </header>

  <div class="abs hero" role="img" aria-label="Family at home while the father uses a wall-mounted security touch panel"></div>
  <div class="abs band"></div>

  <div class="abs slogan slogan-1">LET US</div>
  <div class="abs slogan slogan-2">HELP YOU</div>
  <div class="abs slogan slogan-3">PROTECT YOUR HOME</div>

  <h1 class="abs welcome">Welcome</h1>
  <section class="abs intro">
    <p>Fusce nibh erat, accumsan eu lobortis scelerisque, imperdiet sed odio. Praesent non felis felis. In gravida consectetur mattis. Morbi ultrices, mi at semper facilisis, tortor ligula lacinia lorem, a rhoncus neque ipsum ut velit. Aenean fermentum, urna at tincidunt porta, nisi nulla congue arcu, id viverra elit lorem vel metus. Maecenas varius porta nulla sed sollicitudin. Aliquam vel imperdiet sem. Ut neque nunc, suscipit eget condimentum at, porttitor non orci. Aliquam tortor purus, scelerisque ut vulputate sit amet, adipiscing a lorem.</p>
  </section>

  <aside class="abs callbox">
    <div class="abs call-title">CALL NOW</div>
    <div class="abs call-phone">
      <svg width="26" height="30" viewBox="0 0 26 30"><path d="M6 2 L11 2 L12 9 L8 11 C9 16 12 20 16 22 L19 18 L25 21 L24 27 C15 29 3 18 3 6 Z" fill="#fff"/></svg>
      <span>800-555-0142</span>
    </div>
    <div class="field" style="top:99px">First Name</div>
    <div class="field" style="top:132px">Last Name</div>
    <div class="field" style="top:165px">Email Address</div>
    <div class="field" style="top:199px;height:77px">Message</div>
    <div class="abs submit">SUBMIT</div>
  </aside>

  <section class="abs products">
    <div class="product" style="left:0;width:140px">WIRELESS ALARMS<div class="shot" role="img" aria-label="Wireless alarm kit"></div></div>
    <div class="product" style="left:140px;width:159px">HARDWARE ALARMS<div class="shot" role="img" aria-label="Hardwired alarm panel and sensors"></div></div>
    <div class="product" style="left:299px;width:158px">SECURITY CAMERAS<div class="shot" role="img" aria-label="Outdoor security camera"></div></div>
    <div class="product" style="left:457px;width:154px">DRIVEWAY ALARMS<div class="shot" role="img" aria-label="Driveway motion sensor and receiver"></div></div>
    <div class="product" style="left:611px;width:183px">PERSONAL PROTECTION<div class="shot" role="img" aria-label="Handheld personal protection device"></div></div>
    <div class="product" style="left:794px;width:144px">EXCLUSIVE BUNDLES<div class="shot" role="img" aria-label="Complete security bundle"></div></div>
  </section>

  <footer class="abs footer">
    <span class="copy">Copyright © 2013 Porchlight Partners. All Rights Reserved. User Agreement and Privacy Policy.</span>
    <span class="links">About Us &nbsp;|&nbsp; Contact Us &nbsp;| Sitemap</span>
  </footer>
</div>
</body>
</html>
```